Need someone to revamp my signboard

I own a Manicure Salon. The current signboard design is very clean in look with black and white to complement my shop design. But my shop is undergoing a major reno and the new design is more feminine, elegant with wooden flooring and white cabinets. VELOURIA by Pearl & Fern is the name of the shop. Pearl and Fern is the holding company. So I would like it to be incorporated in the signage too.
The new colour should be beige, brown with hint of red to communicate feminine as well as elegant feel.

```html
<!DOCTYPE html>
<html lang="en">
<head>
<meta charset="utf-8">
<title>VELOURIA by Pearl &amp; Fern — Signboard</title>
<link rel="stylesheet" href="https://fonts.googleapis.com/css2?family=Josefin+Sans:wght@600&family=Parisienne&family=Cormorant+Garamond:wght@500&display=swap">
<style>
  :root {
    --page-bg: #ffffff;
    --board-beige: #f7dea5;
    --brand-brown: #5e2a1a;
    --accent-red: #e02222;
    --board-shadow: rgba(0, 0, 0, 0.45);
  }
  html, body {
    margin: 0;
    padding: 0;
    width: 1200px;
    height: 1000px;
    overflow: hidden;
    background: var(--page-bg);
  }
  .signboard {
    display: block;
    width: 1200px;
    height: 1000px;
  }
  .board-panel { fill: var(--board-beige); }
  .accent-rule { stroke: var(--accent-red); stroke-width: 3.5; }
  .shop-name {
    font-family: "Josefin Sans", "Century Gothic", sans-serif;
    font-weight: 600;
    font-size: 190px;
    fill: var(--brand-brown);
  }
  .tagline {
    font-family: "Parisienne", "Brush Script MT", cursive;
    font-size: 34px;
    fill: var(--brand-brown);
  }
  .holding-company {
    font-family: "Cormorant Garamond", "Times New Roman", serif;
    font-weight: 500;
    fill: var(--brand-brown);
  }
  .holding-company .connector { font-size: 25px; }
  .holding-company .initial { font-size: 62px; }
  .holding-company .small-cap { font-size: 47px; }
</style>
</head>
<body>
<svg class="signboard" viewBox="0 0 1200 1000" xmlns="http://www.w3.org/2000/svg">
  <defs>
    <filter id="board-drop" x="-5%" y="-10%" width="115%" height="130%">
      <feDropShadow dx="10" dy="8" stdDeviation="6" flood-color="var(--board-shadow)" flood-opacity="0.5"/>
    </filter>
  </defs>

  <rect class="board-panel" x="60" y="327" width="1080" height="330" filter="url(#board-drop)"/>

  <text class="shop-name" x="120" y="508" textLength="975" lengthAdjust="spacingAndGlyphs">VELOURIA</text>

  <line class="accent-rule" x1="60" y1="543" x2="1140" y2="543"/>
  <line class="accent-rule" x1="60" y1="622" x2="1140" y2="622"/>

  <text class="tagline" x="108" y="596" textLength="440" lengthAdjust="spacingAndGlyphs">Elegance In Every Detail</text>

  <text class="holding-company" x="580" y="604" textLength="515" lengthAdjust="spacingAndGlyphs"><tspan class="connector" dy="-30">BY</tspan><tspan class="initial" dy="30" dx="8">P</tspan><tspan class="small-cap">EARL</tspan><tspan class="connector" dx="10">AND</tspan><tspan class="initial" dx="10">F</tspan><tspan class="small-cap">ERN</tspan></text>
</svg>
</body>
</html>
```